Psychology practice - information brochure/flyer - half A4 page folded (4 sides)

We need a brochure/flyer to market our psychology service to GPs (Doctors). We need to demonstrate to the doctors that we are the right choice for their patients, and that we cover a large range of services so all of their patients needs are met. We will demonstrate this by listing our range of services and our team of psychologists. We have two locations in Sydney and offer high end services. I've attached our company logo but we remain flexible regarding the style of the brochures. I will provide more details (services, locations & psychologist credentials) once our preferred brochure design has been selected.

```html
<!DOCTYPE html>
<html lang="en">
<head>
<meta charset="utf-8">
<title>Clear Path Clinical Psychology – GP Flyer</title>
<link rel="stylesheet" href="https://fonts.googleapis.com/css2?family=Jost:wght@400;500;700&display=swap">
<style>
  :root {
    --stage: #707070;
    --cream: #f6f1e1;
    --yellow: #f7c21a;
    --yellow-deep: #f0a81c;
    --teal: #5bbfcc;
    --grey: #666666;
    --ink: #3f3f3f;
    --white: #ffffff;
    --page-w: 520px;
    --page-h: 735px;
  }
  * { box-sizing: border-box; margin: 0; padding: 0; }
  html, body { width: 1200px; height: 794px; overflow: hidden; }
  body {
    background: var(--stage);
    font-family: "Jost", Arial, sans-serif;
    color: var(--ink);
    position: relative;
  }
  .page {
    position: absolute;
    top: 30px;
    width: var(--page-w);
    height: var(--page-h);
    background: var(--cream);
    overflow: hidden;
    box-shadow: 0 6px 18px rgba(0,0,0,.35);
  }
  .page--back { left: 50px; }
  .page--front { left: 630px; }
  .page-bg { position: absolute; inset: 0; width: 100%; height: 100%; }
  .block { position: absolute; }

  /* back page */
  .section-title { font-weight: 700; font-size: 16px; margin-bottom: 5px; }
  .on-dark { color: var(--white); }
  .clinicians { left: 28px; top: 16px; width: 380px; }
  .clinician { margin-bottom: 5px; line-height: 1.15; }
  .clinician-name { font-weight: 700; font-size: 12.5px; }
  .clinician-creds { font-size: 10px; opacity: .9; }
  .fees { left: 28px; top: 214px; width: 390px; font-size: 10.5px; line-height: 13px; }
  .fees .section-title { margin-bottom: 3px; }
  .fee-heading { font-weight: 700; font-style: italic; }
  .fee-list { list-style: none; margin-bottom: 3px; }
  .fee-list li::before { content: "• "; }
  .groups { left: 28px; top: 358px; width: 380px; }
  .group-list { list-style: none; columns: 2; font-size: 11px; line-height: 14px; }
  .group-list li::before { content: "• "; }
  .banner { left: 22px; top: 470px; width: 280px; font-weight: 700; font-size: 14px; line-height: 17px; color: var(--ink); }
  .services { left: 28px; top: 524px; width: 210px; }
  .services .section-title, .hours .section-title { color: var(--ink); font-size: 14px; }
  .service-list { list-style: none; font-size: 11px; line-height: 14px; }
  .service-list li::before { content: "• "; color: var(--teal); }
  .hours { left: 260px; top: 524px; width: 240px; font-size: 13px; font-weight: 700; line-height: 18px; }
  .contact { left: 28px; top: 646px; width: 390px; font-size: 10.5px; line-height: 13px; color: var(--white); }
  .contact-title { font-weight: 700; font-size: 13px; }
  .contact-phone { font-weight: 700; font-size: 12.5px; margin-top: 2px; }
  .icon-badge { position: absolute; width: 52px; height: 52px; }

  /* front page */
  .brand { right: 34px; top: 92px; display: flex; align-items: center; gap: 10px; }
  .brand-dot { width: 22px; height: 22px; border-radius: 50%; background: var(--yellow); flex: none; }
  .brand-name { font-weight: 500; font-size: 27px; line-height: 28px; color: var(--ink); }
  .headline { left: 36px; top: 198px; font-size: 29px; line-height: 31px; font-weight: 400; color: var(--ink); }
  .headline strong { font-weight: 700; }
  .web { right: 30px; top: 334px; font-size: 13px; font-weight: 700; color: var(--ink); }
</style>
</head>
<body>

<section class="page page--back" aria-label="Flyer back">
  <svg class="page-bg" viewBox="0 0 520 735" aria-hidden="true">
    <polygon points="0,0 520,0 520,190 0,210" fill="var(--grey)"/>
    <polygon points="0,210 520,190 520,330 0,350" fill="var(--teal)"/>
    <polygon points="0,350 520,330 520,440 0,460" fill="var(--grey)"/>
    <polygon points="0,464 300,464 318,490 300,516 0,516" fill="var(--yellow)"/>
    <polygon points="0,640 520,618 520,735 0,735" fill="var(--teal)"/>
  </svg>

  <div class="block clinicians on-dark">
    <h2 class="section-title">Our Clinicians</h2>
    <div class="clinician"><div class="clinician-name">Dr Helena Varga</div><div class="clinician-creds">BPsych(Hons), MClinPsych, MAPS</div></div>
    <div class="clinician"><div class="clinician-name">Mr Owen Castell</div><div class="clinician-creds">PhD(Psych), MClinPsych, FCCLP</div></div>
    <div class="clinician"><div class="clinician-name">Tessa Quinlan</div><div class="clinician-creds">BPsych(Hons), MPsych(Clin)</div></div>
    <div class="clinician"><div class="clinician-name">Priya Desai</div><div class="clinician-creds">BPsych(Hons), MAPS</div></div>
    <div class="clinician"><div class="clinician-name">Claire Benton</div><div class="clinician-creds">BPsych(Hons), MClinPsych, MAPS</div></div>
  </div>

  <svg class="icon-badge" style="left:432px;top:52px" viewBox="0 0 52 52" aria-hidden="true">
    <circle cx="26" cy="26" r="25" fill="var(--yellow)" stroke="var(--white)" stroke-width="2"/>
    <circle cx="26" cy="20" r="7" fill="var(--ink)"/><path d="M13 38 q13-16 26 0z" fill="var(--ink)"/>
  </svg>
  <svg class="icon-badge" style="left:432px;top:122px" viewBox="0 0 52 52" aria-hidden="true">
    <circle cx="26" cy="26" r="25" fill="var(--white)"/>
    <circle cx="26" cy="20" r="7" fill="var(--teal)"/><path d="M13 38 q13-16 26 0z" fill="var(--teal)"/>
  </svg>

  <div class="block fees on-dark">
    <h2 class="section-title">Our Fee Structure</h2>
    <p class="fee-heading">Business Hours – 9am to 5pm</p>
    <ul class="fee-list">
      <li>$150 per session for General Psychologist, with Medicare Rebate of $88</li>
      <li>$210 per session for Clinical Psychologist, with Medicare Rebate of $129</li>
    </ul>
    <p class="fee-heading">Out of hours – weekends and after 5pm</p>
    <ul class="fee-list">
      <li>$170 per session for General Psychologist, with Medicare Rebate of $88</li>
      <li>$230 per session for Clinical Psychologist, with Medicare Rebate of $129</li>
    </ul>
  </div>

  <div class="block groups on-dark">
    <h2 class="section-title">Our Client Groups:</h2>
    <ul class="group-list">
      <li>Children 5-12</li><li>Adolescents</li><li>Adults</li><li>Veterans</li>
      <li>Victims of crime</li><li>Injured workers</li><li>Culturally and Linguistically Diverse backgrounds</li><li>Refugees</li>
    </ul>
  </div>
  <svg class="icon-badge" style="left:432px;top:362px" viewBox="0 0 52 52" aria-hidden="true">
    <circle cx="26" cy="26" r="25" fill="var(--yellow)" stroke="var(--white)" stroke-width="2"/>
    <circle cx="18" cy="21" r="5" fill="var(--ink)"/><circle cx="34" cy="21" r="5" fill="var(--ink)"/>
    <path d="M9 36 q9-12 18 0z M25 36 q9-12 18 0z" fill="var(--ink)"/>
  </svg>

  <p class="block banner">New location opening soon<br>in Kellway St Northmere</p>

  <div class="block services">
    <h2 class="section-title">Type of Services</h2>
    <ul class="service-list">
      <li>Depression and anxiety</li><li>Trauma and PTSD</li><li>Relationship issues</li><li>Grief and loss</li><li>Eating disorders</li>
    </ul>
  </div>
  <div class="block hours">
    <h2 class="section-title">Hours of Operation</h2>
    <p>Monday – Friday: 9am – 7pm</p>
    <p>Saturday: 9am – 1pm</p>
  </div>

  <div class="block contact">
    <p class="contact-title">To Make Appointments</p>
    <p>Please Contact us on below</p>
    <p>Northmere - Shop 4, 27 Kellway Street 2987</p>
    <p>Westvale - Suite 2, 8 Lorne Street 2981</p>
    <p>e-mail: info@clearpathpsychology.com.au</p>
    <p class="contact-phone">ph. 02 5550 0147 &nbsp;fax. 02 5550 0148</p>
  </div>
  <svg class="icon-badge" style="left:440px;top:640px" viewBox="0 0 52 52" aria-hidden="true">
    <circle cx="26" cy="26" r="25" fill="var(--yellow)" stroke="var(--white)" stroke-width="2"/>
    <path d="M17 14 l6 0 l3 8 l-4 3 q3 7 9 9 l3-4 l8 3 l0 6 q-20 2-25-25z" fill="var(--ink)"/>
  </svg>
</section>

<section class="page page--front" aria-label="Flyer cover">
  <svg class="page-bg" viewBox="0 0 520 735" aria-hidden="true">
    <defs>
      <linearGradient id="session-tones" x1="0" y1="0" x2="1" y2="1">
        <stop offset="0" stop-color="#c9a88a"/>
        <stop offset=".5" stop-color="#e9e4dc"/>
        <stop offset="1" stop-color="#f2efe9"/>
      </linearGradient>
    </defs>
    <polygon points="0,180 520,180 520,330 170,330 150,345 0,345" fill="var(--yellow)"/>
    <polygon points="0,310 150,310 170,326 520,326 520,336 166,336 146,320 0,320" fill="var(--teal)"/>
    <path d="M0,735 L0,430 Q240,360 520,400 L520,735 Z" fill="var(--grey)"/>
    <ellipse cx="300" cy="700" rx="330" ry="270" fill="var(--yellow-deep)"/>
    <ellipse cx="300" cy="700" rx="320" ry="258" fill="var(--yellow)"/>
  </svg>
  <svg class="page-bg" viewBox="0 0 520 735" role="img" aria-label="Photo: a psychologist listening to a client during a counselling session">
    <ellipse cx="290" cy="710" rx="305" ry="242" fill="url(#session-tones)"/>
  </svg>

  <div class="block brand">
    <span class="brand-dot"></span>
    <span class="brand-name">Clear Path<br>Clinical Psychology</span>
  </div>

  <h1 class="block headline">Working together<br>to <strong>achieve</strong> a <strong>better</strong><br>quality of <strong>life</strong></h1>
  <p class="block web">www.clearpathpsychology.com.au</p>
</section>

</body>
</html>
```